A4 Flyer

Bright Path Learning is starting a course in regional Victoria. We are currently advertising (See attached file A34984) in local papers but need to create a one page flyer to distribute to Aged Care facilities in the area. The A4 flyer will be inserted into a folder pack with more detailed information on Bright Path Learning. Important to use images and logoes attached

Target Market(s)

Flyer to be distributed to Aged Care facility staff and owners

Industry/Entity Type

Advertising

Font styles to use
Sans Serif

Colors
f37123
ec1f27

Requirements
Must have
• BPL Logo
Some image

```html
<!DOCTYPE html>
<html lang="en">
<head>
<meta charset="utf-8">
<title>Bright Path Learning – Fast Track Health-training Course</title>
<link rel="stylesheet" href="https://fonts.googleapis.com/css2?family=Arimo:wght@400;700&family=Tinos:wght@700&display=swap">
<style>
  :root {
    --orange: #f37123;
    --red: #ec1f27;
    --deep-red: #e2412e;
    --light-orange: #f68d3c;
    --note-orange: #f7923a;
    --grey: #58595b;
    --ink: #111111;
    --white: #ffffff;
  }
  * { box-sizing: border-box; margin: 0; padding: 0; }
  html, body { width: 848px; height: 1200px; overflow: hidden; }
  body {
    position: relative;
    background: linear-gradient(135deg, var(--light-orange) 0%, var(--orange) 45%, var(--deep-red) 100%);
    font-family: "Arimo", Arial, sans-serif;
    color: var(--ink);
  }
  .header {
    position: absolute; top: 28px; left: 0; width: 100%;
    text-align: center; color: var(--white);
    font-family: "Tinos", "Times New Roman", serif; font-weight: 700;
    text-shadow: 1px 1px 0 #7a3a12, 2px 2px 3px rgba(0,0,0,.45);
  }
  .header__title { font-size: 46px; letter-spacing: 1.5px; line-height: 1.15; }
  .header__subtitle { font-size: 31px; line-height: 1.45; margin-top: 4px; }
  .hero {
    position: absolute; left: 215px; top: 205px; width: 585px; height: 278px;
    background: linear-gradient(90deg, #d9d3cc 0%, #8e8277 35%, #b9b4ae 60%, #f2f0ee 100%);
  }
  .hero-shelf {
    position: absolute; left: 44px; top: 472px; width: 752px; height: 12px;
    background: var(--white); box-shadow: 0 3px 6px rgba(0,0,0,.2);
  }
  .panel {
    position: absolute; left: 44px; top: 505px; width: 761px; height: 647px;
    background: var(--white);
  }
  .panel__headline {
    position: absolute; top: 30px; left: 0; width: 100%; text-align: center;
    font-family: "Tinos", "Times New Roman", serif; font-weight: 700;
    color: var(--red); font-size: 25px; line-height: 34px;
  }
  .funding {
    position: absolute; left: 42px; top: 114px;
    font-size: 22px; font-weight: 700; line-height: 29px;
  }
  .enrol { position: absolute; left: 42px; top: 190px; font-weight: 700; }
  .enrol__label { color: var(--red); font-size: 21px; }
  .enrol__web { color: var(--grey); font-size: 31px; margin-top: 2px; }
  .enrol__phone { color: var(--red); font-size: 33px; margin-top: -2px; }
  .venue-note {
    position: absolute; left: 472px; top: 118px; width: 262px; height: 165px;
    background: var(--note-orange); transform: rotate(-1.5deg);
    box-shadow: 4px 5px 8px rgba(0,0,0,.35);
    display: flex; align-items: center; justify-content: center;
    text-align: center; font-size: 23px; font-weight: 700; line-height: 30px;
  }
  .funding-note {
    position: absolute; left: 42px; top: 325px; width: 690px;
    font-family: "Tinos", "Times New Roman", serif; font-weight: 700;
    font-size: 19px; line-height: 28px;
  }
  .topics {
    position: absolute; left: 70px; top: 385px; width: 680px;
    list-style: none; display: flex; flex-wrap: wrap;
    font-size: 20px; font-weight: 700; line-height: 27px;
  }
  .topics li { margin-right: 16px; display: flex; align-items: center; }
  .topics li::before {
    content: ""; width: 7px; height: 7px; background: var(--red);
    transform: rotate(45deg); margin-right: 10px;
  }
  .topics .break { flex-basis: 100%; height: 0; margin: 0; }
  .topics .break::before { display: none; }
  .brand {
    position: absolute; left: 140px; top: 520px;
    display: flex; align-items: center; gap: 18px;
  }
  .brand__mark { width: 54px; height: 54px; border-radius: 50%; background: var(--orange); }
  .brand__name { color: var(--orange); font-size: 50px; font-weight: 400; letter-spacing: 1px; }
  .toid {
    position: absolute; left: 612px; top: 605px;
    font-family: "Tinos", "Times New Roman", serif; font-size: 12px;
  }
</style>
</head>
<body>
  <header class="header">
    <h1 class="header__title">Unique Opportunity!</h1>
    <p class="header__subtitle">Fast Track Health-training Course -<br>Start July 2014</p>
  </header>

  <div class="hero" role="img" aria-label="Photo of a carer tending to an older man's arm, with medicine bottles, a stethoscope and a wheelchair"></div>
  <div class="hero-shelf"></div>

  <main class="panel">
    <h2 class="panel__headline">DOUBLE QUALIFICATION - CERT III IN AGED CARE<br>WITH HOME AND COMMUNITY CARE</h2>

    <p class="funding">Government Funding for eligible<br>students! Fees from $117</p>

    <div class="enrol">
      <p class="enrol__label">TO ENROL VISIT</p>
      <p class="enrol__web">brightpathlearning.com.au</p>
      <p class="enrol__phone">OR CALL 9800 4512</p>
    </div>

    <div class="venue-note">Hillcrest Nursing<br>Home - Stawell<br>9:00am - 3:00pm</div>

    <p class="funding-note">This training is delivered with VIC and Comm Govt Funding to eligible students.</p>

    <ul class="topics">
      <li>Pathology</li><li>Aged Care</li><li>First Aid</li><li>CPR</li><li>Anaphylaxis</li>
      <li class="break"></li>
      <li>Home &amp; Community Care</li><li>Medications for PCA’s</li>
      <li class="break"></li>
      <li>Health Services</li>
    </ul>

    <div class="brand">
      <span class="brand__mark"></span>
      <span class="brand__name">Bright Path Learning</span>
    </div>
    <p class="toid">Toid 40318</p>
  </main>
</body>
</html>
```